A Lantern on the pier.

I need a book cover (and back cover) design for a novel. The novel is a thiller. ´Synopsis: During the party after an awards ceremony at prestigious institution, one of the young awarders dissapear. The last place where he left a trace was close to a giant chessboard in the grass of the beautiful gardens of the place of ceremony. The detective in charge of finding the missing person and find out what happened will gradually discover that the institution is not all that it seems.
The book cover size will be 9" x 6" and the title of the novel "A lantern on the pier" will be name in spanish "Una linterna en el muelle". The back cover will have a synopsis (in spanish )that i will develop later on.
One suggestion for the design: I always love the art of MILO TRENT for movie posters, so I´m looking for something of similar style, you know (the girl who sold paper kites, North pier ballad, halvorn, ledger of shadows, etc

```html
<!DOCTYPE html>
<html lang="es">
<head>
<meta charset="utf-8">
<title>Una linterna en el muelle — Cubierta</title>
<link rel="stylesheet" href="https://fonts.googleapis.com/css2?family=Patrick+Hand+SC&family=Walter+Turncoat&display=swap">
<style>
  :root {
    --stage: #f1f1f1;
    --cream-top: #fdf0e4;
    --cream-bottom: #e6d9cb;
    --orange: #eea23a;
    --orange-light: #fbc46c;
    --orange-deep: #e79a2e;
    --ink: #17161a;
    --red: #c4242a;
    --white: #ffffff;
  }
  * { box-sizing: border-box; margin: 0; padding: 0; }
  html, body {
    width: 1200px;
    height: 800px;
    overflow: hidden;
    background: var(--stage);
  }
  .spread {
    position: absolute;
    inset: 0;
    display: flex;
    justify-content: center;
    align-items: center;
    gap: 40px;
  }
  .cover {
    position: relative;
    width: 480px;
    height: 720px;
    background: linear-gradient(180deg, var(--cream-top), var(--cream-bottom));
    box-shadow: 0 10px 30px rgba(0,0,0,0.12);
    overflow: hidden;
  }

  /* Back cover */
  .back-panel {
    position: absolute;
    left: 26px;
    top: 30px;
    width: 428px;
    height: 640px;
    background: linear-gradient(180deg, var(--orange-light) 0%, var(--orange-deep) 45%, var(--orange) 100%);
    display: flex;
    flex-direction: column;
    align-items: center;
  }
  .back-title {
    margin-top: 34px;
    font-family: "Patrick Hand SC", sans-serif;
    font-size: 30px;
    letter-spacing: 1px;
    color: var(--white);
  }
  .back-art {
    margin-top: 26px;
    width: 330px;
    height: 190px;
    background: linear-gradient(180deg, rgba(196,36,42,0.0) 0%, var(--red) 40%, var(--red) 70%, var(--ink) 100%);
    clip-path: polygon(0 78%, 12% 30%, 30% 20%, 50% 8%, 70% 2%, 88% 10%, 100% 30%, 100% 82%, 60% 92%, 10% 100%);
  }
  .synopsis {
    margin-top: 34px;
    width: 300px;
    text-align: center;
    font-family: "Walter Turncoat", cursive;
    font-size: 14px;
    line-height: 1.4;
    text-transform: uppercase;
    color: var(--white);
  }

  /* Front cover */
  .front-title {
    position: absolute;
    left: 36px;
    top: 96px;
    font-family: "Patrick Hand SC", sans-serif;
    font-size: 82px;
    line-height: 0.9;
    color: var(--ink);
  }
  .front-title span { display: block; }
  .front-panel {
    position: absolute;
    left: 0;
    top: 0;
    width: 480px;
    height: 720px;
  }
  .front-art {
    position: absolute;
    left: 66px;
    top: 498px;
    width: 340px;
    height: 158px;
    background: linear-gradient(180deg, rgba(196,36,42,0.0) 0%, var(--red) 35%, var(--red) 65%, var(--ink) 100%);
    clip-path: polygon(0 45%, 14% 20%, 40% 12%, 58% 0, 76% 18%, 100% 40%, 98% 100%, 50% 80%, 6% 62%);
  }
</style>
</head>
<body>
  <main class="spread">
    <section class="cover cover--back" aria-label="Contracubierta">
      <div class="back-panel">
        <h2 class="back-title">UNA LINTERNA EN EL MUELLE</h2>
        <div class="back-art" role="img" aria-label="Siluetas rojas de piezas de ajedrez entre hierba negra y flores"></div>
        <p class="synopsis">During the party after an awards ceremony at a prestigious institution, one of the young awardees disappears. The last place where he left a trace was close to a giant chessboard in the grass of the gardens of the place of ceremony. The detective in charge of finding the missing person and finding out what happened will gradually discover that the institution is not all that it seems.</p>
      </div>
    </section>

    <section class="cover cover--front" aria-label="Cubierta">
      <h1 class="front-title">
        <span>UNA</span>
        <span>LINTERNA</span>
        <span>EN EL</span>
        <span>MUELLE</span>
      </h1>
      <svg class="front-panel" viewBox="0 0 480 720" aria-hidden="true">
        <path d="M20 420 C120 440 220 462 300 478 C340 484 380 492 460 510 L448 700 C330 670 150 620 28 596 Z" fill="var(--orange)"/>
      </svg>
      <div class="front-art" role="img" aria-label="Siluetas rojas de piezas de ajedrez entre hierba negra y flores"></div>
    </section>
  </main>
</body>
</html>
```